Window Treatment specialists need business card design

We are moving into a new location and want to highlight our expertise and all we have to offer. We are now a Larkmoor Fennick Gallery for customized window treatments. We also offer custom soft treatments i.e drapery, valances, cornices, upholstery, pillows, color design services, outdoor fabrics, and specialize in motorization of hard treatments.

Target Market(s)

Home Owners 30- 55 with annual income $150,000 and up

Industry/Entity Type

Home Improvement

Contact Information for Business Card

We want our location, name, email, website, phone number, fax, business logo, and Larkmoor Fennick logo on the card. Anything else we are open to the design.

Font styles to use
Sans Serif

Requirements
Must have
• location, name, email, website, phone number, fax, business logo, and Larkmoor Fennick logo on the card. Anything else we are open to the design.

```html
<!DOCTYPE html>
<html lang="en">
<head>
<meta charset="utf-8">
<title>Veyra Studio – Business Cards</title>
<link rel="stylesheet" href="https://fonts.googleapis.com/css2?family=Raleway:wght@400;500;600;700&display=swap">
<style>
  :root {
    --ink: #211e1f;
    --orange: #f38b1f;
    --orange-light: #f7a040;
    --teal: #9ec9cb;
    --white: #ffffff;
    --stage: #262626;
  }
  * { box-sizing: border-box; margin: 0; padding: 0; }
  html, body { width: 1200px; height: 800px; overflow: hidden; }
  body {
    background: var(--stage);
    font-family: "Raleway", sans-serif;
    position: relative;
  }
  .card {
    position: absolute;
    top: 246px;
    width: 540px;
    height: 308px;
    background: var(--orange);
    overflow: hidden;
    color: var(--ink);
  }
  .card--front { left: 40px; }
  .card--back { left: 620px; }
  .card__shape { position: absolute; inset: 0; width: 100%; height: 100%; }

  /* partner mark */
  .partner {
    position: absolute; left: 34px; top: 30px;
    display: flex; align-items: center; gap: 10px;
  }
  .partner__dot { width: 34px; height: 34px; border-radius: 50%; background: var(--orange); }
  .partner__name {
    color: var(--white); font-weight: 700; font-size: 15px; line-height: 1.15;
  }

  /* business name */
  .brand {
    position: absolute; color: var(--teal); font-weight: 600; line-height: 1;
  }
  .card--front .brand { left: 210px; top: 66px; font-size: 30px; }
  .card--back .brand { right: 40px; top: 66px; font-size: 40px; }

  .person { position: absolute; right: 34px; top: 112px; text-align: right; }
  .person__name { color: var(--white); font-size: 19px; font-weight: 500; }
  .person__title { color: var(--orange); font-size: 13px; margin-top: 3px; }

  .contact { position: absolute; font-size: 13px; font-weight: 500; line-height: 1.5; }
  .contact--web { left: 34px; bottom: 46px; }
  .contact--place { right: 34px; bottom: 22px; }
  .contact__row { display: flex; align-items: center; gap: 7px; }
  .contact__row svg { width: 12px; height: 12px; flex: none; }

  .services {
    position: absolute; left: 40px; top: 226px; width: 460px;
    text-align: center; font-size: 12px; font-weight: 500; line-height: 1.45;
  }
</style>
</head>
<body>

<section class="card card--front" aria-label="Card front">
  <svg class="card__shape" viewBox="0 0 540 308" preserveAspectRatio="none" aria-hidden="true">
    <path d="M0,0 H540 V195 C420,188 210,128 0,112 Z" fill="var(--ink)"/>
    <path d="M470,308 C505,280 525,250 540,225 V308 Z" fill="var(--orange-light)"/>
  </svg>

  <div class="partner">
    <span class="partner__dot"></span>
    <span class="partner__name">Larkmoor Fennick<br>Gallery</span>
  </div>

  <div class="brand">Veyra Studio</div>

  <div class="person">
    <div class="person__name">Your name here</div>
    <div class="person__title">Title here</div>
  </div>

  <div class="contact contact--web">
    <div class="contact__row">
      <svg viewBox="0 0 12 12"><rect x="0.5" y="2" width="11" height="8" fill="var(--ink)"/><path d="M0.5,2 L6,7 L11.5,2" stroke="var(--orange)" fill="none"/></svg>
      mailaddress@email.com
    </div>
    <div class="contact__row">
      <svg viewBox="0 0 12 12"><circle cx="6" cy="6" r="5.5" fill="var(--ink)"/><path d="M0.5,6 H11.5 M6,0.5 C3,4 3,8 6,11.5 M6,0.5 C9,4 9,8 6,11.5" stroke="var(--orange)" fill="none" stroke-width="0.8"/></svg>
      www.yourwebsite.com
    </div>
  </div>

  <div class="contact contact--place">
    <div>location here, location here</div>
    <div>location here</div>
    <div class="contact__row">
      <svg viewBox="0 0 12 12"><path d="M2,1 L4.5,1 L5.5,4 L4,5 C5,7 6,8 7.5,8.5 L8.5,7 L11,8 L11,10.5 C6,11 1,6 2,1 Z" fill="var(--ink)"/></svg>
      0223-4456-3334
    </div>
    <div class="contact__row">
      <svg viewBox="0 0 12 12"><rect x="3" y="1" width="6" height="4" fill="var(--ink)"/><rect x="1" y="5" width="10" height="6" rx="1" fill="var(--ink)"/><rect x="3" y="7" width="6" height="1.5" fill="var(--orange)"/></svg>
      4434-4455-3346
    </div>
  </div>
</section>

<section class="card card--back" aria-label="Card back">
  <svg class="card__shape" viewBox="0 0 540 308" preserveAspectRatio="none" aria-hidden="true">
    <path d="M90,0 H540 V196 C400,204 190,150 90,0 Z" fill="var(--ink)"/>
  </svg>

  <div class="brand">Veyra Studio</div>

  <p class="services">Custom soft treatments i.e drapery, valances, cornices, upholstery, pillows color design services, outdoor fabrics and specialize in motorization of hard treatments.</p>
</section>

</body>
</html>
```